Dr. Marisa Tellen Medical/Chiropractic Business Card

Dr. Tellen is a chiropractor and will require a business card that she uses every single day to book appointments on the back side of the card. Currently the office name goes by Dr. Marisa Tellen. The chiropractic profession is based on the diagnosis and manipulative treatment of misalignments of the joints, especially those of the spinal column, which are held to cause other disorders by affecting the nerves, muscles, and organs. Dr. Marisa Tellen is looking for a contemporary and minimalistic design.

Industry/Entity Type

Medical

Contact Information for Business Card

Name: Dr. Marisa Tellen; Address: 748 Ashcombe Rd North, London, ON N5R 2K9; Phone Number: 519.672.4193; Fax: 519.681.2054; email: marisa.tellen@brevanmail.com

Requirements
Must have
• ability to write multiple appointments date/time on the back of card

```html
<!DOCTYPE html>
<html lang="en">
<head>
<meta charset="utf-8">
<title>Dr. Marisa Tellen – Business Card</title>
<link rel="stylesheet" href="https://fonts.googleapis.com/css2?family=Open+Sans:wght@400;600;700&family=Roboto:wght@400&family=Pinyon+Script&display=swap">
<style>
  :root {
    --backdrop: #ece8e2;
    --kraft-light: #c4a57a;
    --kraft: #b3936a;
    --kraft-dark: #a4845c;
    --ink: #17120d;
    --field: #ffffff;
  }
  * { box-sizing: border-box; margin: 0; padding: 0; }
  html, body { width: 1200px; height: 900px; overflow: hidden; }
  body {
    position: relative;
    background: var(--backdrop);
    font-family: "Open Sans", Arial, sans-serif;
    color: var(--ink);
  }
  .card {
    position: absolute;
    background: linear-gradient(160deg, var(--kraft-light) 0%, var(--kraft) 55%, var(--kraft-dark) 100%);
    box-shadow: 0 6px 18px rgba(0,0,0,0.18);
  }
  .card--front { left: 238px; top: 62px; width: 555px; height: 342px; }
  .card--back  { left: 458px; top: 519px; width: 559px; height: 342px; }

  .brand { position: absolute; left: 0; right: 0; text-align: center; color: var(--ink); }
  .brand__inner { display: inline-block; text-align: left; }
  .brand__title { display: block; font-family: "Pinyon Script", cursive; line-height: 1; }
  .brand__name { display: block; font-family: "Roboto", Arial, sans-serif; font-weight: 400; white-space: nowrap; line-height: 1; }
  .card--front .brand { top: 50px; }
  .card--front .brand__title { font-size: 32px; height: 36px; }
  .card--front .brand__name { font-size: 33px; margin-top: 4px; }
  .card--back .brand { top: 34px; }
  .card--back .brand__title { font-size: 26px; height: 29px; }
  .card--back .brand__name { font-size: 26px; margin-top: 2px; }

  .flourish {
    position: absolute;
    background: linear-gradient(90deg, rgba(23,18,13,0) 0%, rgba(23,18,13,0.75) 20%, rgba(23,18,13,0.75) 80%, rgba(23,18,13,0) 100%);
    border-radius: 50%;
  }
  .card--front .flourish { left: 158px; top: 136px; width: 244px; height: 16px; }
  .card--back .flourish { left: 186px; top: 99px; width: 190px; height: 14px; }

  .person { position: absolute; left: 0; right: 0; top: 184px; text-align: center; }
  .person__name { font-size: 18px; font-weight: 700; line-height: 1.2; }
  .person__role { font-size: 14.5px; line-height: 1.3; }

  .contact { position: absolute; left: 0; right: 0; top: 238px; display: flex; flex-direction: column; align-items: center; gap: 2px; list-style: none; }
  .contact__item { display: flex; align-items: center; gap: 7px; font-size: 14px; line-height: 18px; white-space: nowrap; }
  .contact__icon { width: 12px; height: 12px; fill: var(--ink); flex: none; }

  .appointment__heading { position: absolute; left: 0; right: 0; top: 142px; text-align: center; font-size: 18.5px; font-weight: 600; }
  .appointment__row { position: absolute; left: 0; display: flex; align-items: center; }
  .appointment__label { text-align: right; font-size: 14px; font-weight: 600; padding-right: 3px; }
  .label--lead { width: 168px; }
  .label--time { width: 50px; }
  .appointment__field { height: 18px; background: var(--field); }
  .field--name { width: 273px; }
  .field--date { width: 135px; }
  .field--time { width: 88px; }
  .row--name { top: 176px; }
  .row--1 { top: 204px; }
  .row--2 { top: 230px; }
  .row--3 { top: 256px; }
  .appointment__notice { position: absolute; left: 0; right: 0; top: 292px; text-align: center; font-size: 15px; }
</style>
</head>
<body>
  <section class="card card--front" aria-label="Business card front">
    <div class="brand">
      <div class="brand__inner">
        <span class="brand__title">Dr.</span>
        <span class="brand__name">MARISA TELLEN</span>
      </div>
    </div>
    <div class="flourish" role="img" aria-label="Decorative flourish beneath the name"></div>
    <div class="person">
      <p class="person__name">Daniel Hargrove</p>
      <p class="person__role">Managing Director</p>
    </div>
    <ul class="contact">
      <li class="contact__item">
        <svg class="contact__icon" viewBox="0 0 24 24" aria-hidden="true"><path d="M12 2C8.1 2 5 5.1 5 9c0 5.2 7 13 7 13s7-7.8 7-13c0-3.9-3.1-7-7-7zm0 9.5a2.5 2.5 0 1 1 0-5 2.5 2.5 0 0 1 0 5z"/></svg>
        <span>748 Ashcombe Rd North, London, ON N5R 2K9</span>
      </li>
      <li class="contact__item">
        <svg class="contact__icon" viewBox="0 0 24 24" aria-hidden="true"><path d="M6.6 10.8c1.4 2.8 3.8 5.1 6.6 6.6l2.2-2.2c.3-.3.7-.4 1-.2 1.1.4 2.3.6 3.6.6.6 0 1 .4 1 1V20c0 .6-.4 1-1 1C10.6 21 3 13.4 3 4c0-.6.4-1 1-1h3.5c.6 0 1 .4 1 1 0 1.3.2 2.5.6 3.6.1.3 0 .7-.2 1L6.6 10.8z"/></svg>
        <span>Tel 519.672.4193 &nbsp;·&nbsp; Fax 519.681.2054</span>
      </li>
      <li class="contact__item">
        <svg class="contact__icon" viewBox="0 0 24 24" aria-hidden="true"><path d="M2 5h20v2.2l-10 7-10-7z"/><path d="M2 9.6l10 7 10-7V19H2z"/></svg>
        <span>marisa.tellen@brevanmail.com</span>
      </li>
      <li class="contact__item">
        <svg class="contact__icon" viewBox="0 0 24 24" aria-hidden="true"><circle cx="12" cy="12" r="10"/><path d="M12 2v20M2 12h20" stroke="#b3936a" stroke-width="1.6"/></svg>
        <span>www.tellenchiro.com</span>
      </li>
    </ul>
  </section>

  <section class="card card--back" aria-label="Business card back – appointment card">
    <div class="brand">
      <div class="brand__inner">
        <span class="brand__title">Dr.</span>
        <span class="brand__name">MARISA TELLEN</span>
      </div>
    </div>
    <div class="flourish" role="img" aria-label="Decorative flourish beneath the name"></div>
    <h2 class="appointment__heading">Your Next Appointments are</h2>
    <div class="appointment__row row--name"><span class="appointment__label label--lead">Name:</span><span class="appointment__field field--name"></span></div>
    <div class="appointment__row row--1"><span class="appointment__label label--lead">Date:</span><span class="appointment__field field--date"></span><span class="appointment__label label--time">Time:</span><span class="appointment__field field--time"></span></div>
    <div class="appointment__row row--2"><span class="appointment__label label--lead">Date:</span><span class="appointment__field field--date"></span><span class="appointment__label label--time">Time:</span><span class="appointment__field field--time"></span></div>
    <div class="appointment__row row--3"><span class="appointment__label label--lead">Date:</span><span class="appointment__field field--date"></span><span class="appointment__label label--time">Time:</span><span class="appointment__field field--time"></span></div>
    <p class="appointment__notice">If unable to keep appointment, kindly give 24hrs notice.</p>
  </section>
</body>
</html>
```